Gold Award for Hygiene Excellence

We are providing food safety consultancy to restaurant business in the uk. We would like to prepare an award sticker for business that work with us to get sticker award if they got 5 star hygiene rating consecutively in the their last 3 inspections. Normally, they display hygiene scores that are green color on their shop's window. So it should be catchy color for people easily detect the award. Size A5

```html
<!DOCTYPE html>
<html lang="en">
<head>
<meta charset="utf-8">
<title>Gold Award for Hygiene Excellence</title>
<link href="https://fonts.googleapis.com/css2?family=Questrial&family=Jost:wght@700&family=Open+Sans:wght@400;700&display=swap" rel="stylesheet">
<style>
  :root {
    --gold: #fab900;
    --ink: #1f1a1d;
    --paper: #ffffff;
    --grey: #8a8a8a;
    --rule: #6b6b6b;
  }
  html, body { margin: 0; padding: 0; overflow: hidden; background: var(--paper); }
  .sheet { display: block; width: 849px; height: 1200px; }
  .ink { fill: var(--ink); }
  .gold { fill: var(--gold); }
  .paper { fill: var(--paper); }
  .headline { font-family: "Questrial", "Century Gothic", sans-serif; fill: var(--gold); }
  .tagline { font-family: "Jost", "Futura", sans-serif; font-weight: 700; fill: var(--gold); }
  .criteria { font-family: "Questrial", "Century Gothic", sans-serif; font-size: 19px; fill: var(--ink); }
  .score-digit { font-family: "Questrial", "Century Gothic", sans-serif; font-size: 122px; fill: var(--gold); text-anchor: middle; }
  .brand-name { font-family: "Questrial", "Century Gothic", sans-serif; font-size: 40px; fill: var(--grey); }
  .emblem-area { fill: var(--gold); }
  .back-card { fill: var(--paper); stroke: var(--rule); stroke-width: 1.5; }
  .company { font-family: "Open Sans", sans-serif; font-weight: 700; font-size: 24px; fill: var(--ink); text-anchor: middle; }
  .contact { font-family: "Open Sans", sans-serif; font-weight: 400; fill: var(--ink); text-anchor: middle; }
  .divider { stroke: var(--rule); stroke-width: 2; }
</style>
</head>
<body>
<svg class="sheet" viewBox="0 0 1240 1754" xmlns="http://www.w3.org/2000/svg">
  <defs>
    <clipPath id="award-shape">
      <rect x="178" y="231" width="885" height="624" rx="30"/>
    </clipPath>
  </defs>

  <g class="award-front" clip-path="url(#award-shape)">
    <rect class="ink" x="178" y="231" width="885" height="350"/>
    <rect class="paper" x="178" y="581" width="885" height="100"/>
    <rect class="gold" x="178" y="681" width="885" height="174"/>

    <text class="headline" x="236" y="450" font-size="252" textLength="769" lengthAdjust="spacingAndGlyphs">GOLD</text>

    <rect class="emblem-area" x="252" y="462" width="158" height="104" role="img" aria-label="Award ribbon tails hanging below the G"/>

    <text class="headline" x="450" y="558" font-size="118" textLength="480" lengthAdjust="spacingAndGlyphs">AWARD</text>

    <text class="tagline" x="210" y="656" font-size="64" textLength="825" lengthAdjust="spacing">FOR HYGIENE EXCELLENCE</text>

    <g class="criteria-text">
      <text class="criteria" x="210" y="742">THIS AWARD HAS</text>
      <text class="criteria" x="210" y="763">BEEN GIVEN FOR</text>
      <text class="criteria" x="210" y="784">3 CONSECUTIVE</text>
      <text class="criteria" x="210" y="806">5 STAR HYGIENE SCORE</text>
    </g>

    <rect class="paper brand-band" x="790" y="727" width="273" height="81"/>
    <text class="brand-name" x="835" y="782" textLength="198" lengthAdjust="spacing">HALVERN</text>

    <g class="score-badges">
      <circle class="ink" cx="495" cy="768" r="57"/>
      <circle class="ink" cx="620" cy="768" r="57"/>
      <circle class="ink" cx="745" cy="768" r="57"/>
      <text class="score-digit" x="495" y="806">5</text>
      <text class="score-digit" x="620" y="806">5</text>
      <text class="score-digit" x="745" y="806">5</text>
    </g>
  </g>

  <g class="award-back">
    <rect class="back-card" x="178" y="897" width="885" height="624" rx="30"/>
    <text class="company" x="620" y="1384">HALVERN SOLUTIONS LIMITED</text>
    <line class="divider" x1="441" y1="1397" x2="799" y2="1397"/>
    <text class="contact" x="620" y="1426" font-size="26">info@halvernsolutions.co.uk</text>
    <text class="contact" x="620" y="1471" font-size="50">020 3946 0172</text>
  </g>
</svg>
</body>
</html>
```